Endocrinologist needs new stationery

I have a logo from MarkForge and now need stationery with the new logo.

Address: Suite 4, 282 Falcon Street, Elmbrook, VIC 3187
Phone: 03 9417 2253
Fax: 03 9417 2255
Website: www.drmaylacorwen.com.au
Email: admin@drmaylacorwen.com.au

```html
<!DOCTYPE html>
<html lang="en">
<head>
<meta charset="utf-8">
<title>Dr Mayla Corwen – Stationery</title>
<link rel="stylesheet" href="https://fonts.googleapis.com/css2?family=Open+Sans:wght@400&display=swap">
<style>
  :root {
    --backdrop: #ecebe9;
    --paper: #ffffff;
    --brand-blue: #2b5c94;
    --plum: #7e5770;
    --rule: #8d6e82;
    --ink: #4a4a4a;
    --faint-blue: #d9e5f1;
    --faint-plum: #9a7790;
  }
  * { margin: 0; padding: 0; box-sizing: border-box; }
  html, body { width: 1200px; height: 800px; overflow: hidden; }
  body {
    position: relative;
    background: var(--backdrop);
    font-family: "Open Sans", Arial, sans-serif;
    color: var(--ink);
  }
  .sheet { position: absolute; background: var(--paper); overflow: hidden; }
  .brand-name {
    position: absolute;
    color: var(--brand-blue);
    font-weight: 400;
    white-space: nowrap;
    letter-spacing: 0.01em;
  }
  .rule { position: absolute; height: 1px; background: var(--rule); }
  .contact {
    position: absolute;
    display: flex;
    align-items: center;
    white-space: nowrap;
    line-height: 1;
  }
  .contact svg { flex: none; }

  /* Letterhead */
  .letterhead { left: 70px; top: 56px; width: 476px; height: 683px; }
  .letterhead .brand-name { left: 64px; top: 52px; font-size: 36px; }
  .letterhead .rule { left: 44px; top: 564px; width: 389px; }
  .letterhead .contact { font-size: 10px; gap: 10px; }
  .letterhead .contact svg { width: 16px; height: 16px; }

  /* Business card front */
  .card-front { left: 613px; top: 69px; width: 306px; height: 189px; }
  .card-front .brand-name { left: 40px; top: 22px; font-size: 25px; }
  .card-front .contact { font-size: 9.6px; gap: 8px; }
  .card-front .contact svg { width: 14px; height: 14px; }

  /* Business card back */
  .card-back { left: 614px; top: 284px; width: 304px; height: 146px; background: var(--plum); }
  .card-back .mark-shape {
    position: absolute; left: 117px; top: 38px; width: 70px; height: 70px;
    border: 1.5px solid var(--faint-plum); border-radius: 50%;
  }

  /* Compliment slip */
  .slip { left: 575px; top: 466px; width: 578px; height: 273px; }
  .slip .brand-name { left: 30px; top: 32px; font-size: 27px; }
  .slip .mark-shape {
    position: absolute; left: 385px; top: 92px; width: 112px; height: 112px;
    border: 2px solid var(--faint-blue); border-radius: 50%;
  }
  .slip .rule { left: 23px; top: 210px; width: 533px; }
  .slip .contact { font-size: 8.6px; gap: 7px; }
  .slip .contact svg { width: 14px; height: 14px; }
</style>
</head>
<body>

<svg width="0" height="0" style="position:absolute" aria-hidden="true">
  <defs>
    <symbol id="icon-pin" viewBox="0 0 16 16">
      <circle cx="8" cy="8" r="7.3" fill="none" stroke="#7e5770" stroke-width="1"/>
      <path d="M8 3.6a2.9 2.9 0 0 0-2.9 2.9C5.1 9 8 12.4 8 12.4s2.9-3.4 2.9-5.9A2.9 2.9 0 0 0 8 3.6z" fill="#7e5770"/>
      <circle cx="8" cy="6.5" r="1.1" fill="#fff"/>
    </symbol>
    <symbol id="icon-phone" viewBox="0 0 16 16">
      <circle cx="8" cy="8" r="7.3" fill="none" stroke="#7e5770" stroke-width="1"/>
      <path d="M5.6 4.2l1.3-.3.9 2-1 .8c.5 1 1.3 1.8 2.3 2.3l.8-1 2 .9-.3 1.3c-.2.6-.8.9-1.4.8C7.6 10.6 5.4 8.4 4.8 5.6c-.1-.6.2-1.2.8-1.4z" fill="#7e5770"/>
    </symbol>
    <symbol id="icon-fax" viewBox="0 0 16 16">
      <circle cx="8" cy="8" r="7.3" fill="none" stroke="#7e5770" stroke-width="1"/>
      <rect x="5.6" y="4" width="4.8" height="2.4" fill="#7e5770"/>
      <rect x="4.2" y="6.6" width="7.6" height="5" rx="0.8" fill="#7e5770"/>
      <rect x="5.6" y="8.2" width="4.8" height="0.9" fill="#fff"/>
    </symbol>
    <symbol id="icon-web" viewBox="0 0 16 16">
      <circle cx="8" cy="8" r="7.3" fill="none" stroke="#7e5770" stroke-width="1"/>
      <circle cx="8" cy="8" r="4.2" fill="none" stroke="#7e5770" stroke-width="0.9"/>
      <ellipse cx="8" cy="8" rx="1.8" ry="4.2" fill="none" stroke="#7e5770" stroke-width="0.9"/>
      <path d="M3.8 8h8.4M4.5 5.9h7M4.5 10.1h7" stroke="#7e5770" stroke-width="0.8"/>
    </symbol>
    <symbol id="icon-mail" viewBox="0 0 16 16">
      <circle cx="8" cy="8" r="7.3" fill="none" stroke="#7e5770" stroke-width="1"/>
      <rect x="4.3" y="5.3" width="7.4" height="5.4" rx="0.6" fill="#7e5770"/>
      <path d="M4.6 5.7L8 8.4l3.4-2.7" fill="none" stroke="#fff" stroke-width="0.8"/>
    </symbol>
  </defs>
</svg>

<section class="sheet letterhead" aria-label="Letterhead">
  <div class="brand-name">Dr Mayla Corwen</div>
  <div class="rule"></div>
  <div class="contact" style="left:48px;top:582px"><svg><use href="#icon-pin"/></svg>Suite 4, 282 Falcon Street, Elmbrook, VIC 3187</div>
  <div class="contact" style="left:48px;top:606px"><svg><use href="#icon-phone"/></svg>03 9417 2253</div>
  <div class="contact" style="left:155px;top:606px"><svg><use href="#icon-fax"/></svg>03 9417 2255</div>
  <div class="contact" style="left:263px;top:606px"><svg><use href="#icon-web"/></svg>www.drmaylacorwen.com.au</div>
  <div class="contact" style="left:48px;top:633px"><svg><use href="#icon-mail"/></svg>admin@drmaylacorwen.com.au</div>
</section>

<section class="sheet card-front" aria-label="Business card front">
  <div class="brand-name">Dr Mayla Corwen</div>
  <div class="contact" style="left:40px;top:89px"><svg><use href="#icon-pin"/></svg>Suite 4, 282 Falcon Street, Elmbrook, VIC 3187</div>
  <div class="contact" style="left:40px;top:110px"><svg><use href="#icon-phone"/></svg>03 9417 2253</div>
  <div class="contact" style="left:156px;top:110px"><svg><use href="#icon-fax"/></svg>03 9417 2255</div>
  <div class="contact" style="left:40px;top:131px"><svg><use href="#icon-web"/></svg>www.drmaylacorwen.com.au</div>
  <div class="contact" style="left:40px;top:152px"><svg><use href="#icon-mail"/></svg>admin@drmaylacorwen.com.au</div>
</section>

<section class="sheet card-back" aria-label="Business card back">
  <div class="mark-shape"></div>
</section>

<section class="sheet slip" aria-label="Compliment slip">
  <div class="brand-name">Dr Mayla Corwen</div>
  <div class="mark-shape"></div>
  <div class="rule"></div>
  <div class="contact" style="left:33px;top:221px"><svg><use href="#icon-pin"/></svg>Suite 4, 282 Falcon Street, Elmbrook, VIC 3187</div>
  <div class="contact" style="left:33px;top:241px"><svg><use href="#icon-phone"/></svg>03 9417 2253</div>
  <div class="contact" style="left:134px;top:241px"><svg><use href="#icon-fax"/></svg>03 9417 2255</div>
  <div class="contact" style="left:234px;top:241px"><svg><use href="#icon-web"/></svg>www.drmaylacorwen.com.au</div>
  <div class="contact" style="left:400px;top:241px"><svg><use href="#icon-mail"/></svg>admin@drmaylacorwen.com.au</div>
</section>

</body>
</html>
```